Designer Furniture: Brochure Design | Price List | Price Cards

1. brochure 2. price list 3. showroom price cards

We need a brochure design of our high-end wood and acrylic furniture line. We are a custom plastics & acrylics manufacturing company - one facet of our business is custom high-end furniture. We have developed our own proprietary designer furniture line and need a brochure and supporting price list and showroom price cards to reflect the furniture's unique wood and acrylic high-end design appeal.

****More supporting informational & graphic files at:****
https://www.filecrate-share.com/sh/qvbrumtxpkaow7e/pLemRtZdKw

We would like to see the following design style: European, modern, clean lines | Lots of white | warm greys | minimalistic in "graphic design" to show off our "furniture design" as the primary focus of the brochure "less is more" | we work in the high-end design market so our look and feel has to reflect that of 'design' | a screenshot of an example of what we like is included in supplied files | we like modern artwork

This is a North American print distribution. Further detailed instructions & details are supplied in the supporting uploaded files of the project.

The winning design may lead to future exclusive design work in this particular facet of our business - possibly others.

* Price list: should be editable PDF (printed on in-house monochrome laser) that is a secondary insert in to the brochure - B&W 6.75"x8.25" Portrait. Includes each item in table or catalogue-type format with dimensions and pricing "$###.##"

* Showroom price card: editable PDF file for each piece of furniture. 5"x7" Portrait OR Landscape. Should include the main 2D dimensional line drawing of each piece along with dimensions and Brookvale Logo or Icon and QRCode from OLD brochure design.
Updates

*****Supporting files & graphic files at:******

- It is imperative that all 3D renderings from our "Rendering" folder in dropbox link be shown in our brochure.

- The price list is a monochrome listing of all our pieces of furniture with dimensions and prices in a table or catalogue-type format.

Here's to clear up some of the questions you've been asking:

PRICE CARDS:
5"x7" portrait
These cards will be but in to an acrylic stand and sit on each piece of furniture - so would probably be best to design a front and back.
Side #1 with specifics: Product name, product number, dimensions, line drawing, price, Brookvale Logo, QR Code, Contact info
Side #2 the other showcasing 3D image, Product Name, Brookvale logo

PRICE SHEET INSERT:
This is an insert for the brochure cataloguing each of the products, 2D dimensional line drawing, dimensions, product name, product number, price - editable PDF so we can easily change prices and print on our in-house monochrome (black & white) printer. 1 or 2 sided - doesn't matter.  Will fit inside the brochure, so cannot be any larger than 7x8.5 - I would suggest to make .25" smaller than brochure folded size - 6.75x8.25

Target Market(s)

Designers, Architects and High-end Retail Furniture Outlets

Industry/Entity Type

Business

Requirements
Must have
• - Brochure finished folded size must be: 7”w x 8.5”h (PORTRAIT)
- raw print stock is 12.5”x19” – maximum print area is 12”x18.5”
- as long as finished folded size is exactly 7”x8.5” portrait - folding style is up to designer (bifold, 3-panel roll, 4-panel roll)
- Will be digitally printed - RGB on 80lb gloss text
- 3D Render image of each product in the furniture line must be included...see below

****More supporting files & graphic files at:****
Nice to have
• ****Supporting files & graphic files at:****

```html
<!DOCTYPE html>
<html lang="en">
<head>
<meta charset="utf-8">
<title>Brookvale Brochure Spread</title>
<link href="https://fonts.googleapis.com/css2?family=Ubuntu:wght@300;400;500;700&display=swap" rel="stylesheet">
<style>
  :root {
    --canvas: #efece7;
    --page-white: #ffffff;
    --page-fold: #e9e9e9;
    --warm-grey: #7b7472;
    --text-grey: #8a8583;
    --tan: #b89e80;
    --logo-grey: #8e8986;
    --light-line: #f4f2f0;
  }
  * { box-sizing: border-box; margin: 0; padding: 0; }
  html, body {
    width: 1200px; height: 900px; overflow: hidden;
    background: var(--canvas);
    font-family: "Ubuntu", sans-serif;
  }
  .spread {
    position: absolute; left: 50px; top: 117px;
    width: 1100px; height: 666px;
    display: flex;
    box-shadow: 0 2px 8px rgba(0,0,0,0.18);
  }
  .page { position: relative; width: 550px; height: 666px; overflow: hidden; }
  .page--left {
    background: linear-gradient(to right, var(--page-white) 70%, var(--page-fold) 100%);
  }
  .page--right { background: var(--warm-grey); }

  .brand-name {
    position: absolute; left: 38px; top: 40px;
    font-size: 30px; font-weight: 400; color: var(--logo-grey);
    display: flex; align-items: center; gap: 8px;
  }
  .brand-name__dot { width: 12px; height: 12px; border-radius: 50%; background: var(--logo-grey); }

  .intro-headline {
    position: absolute; left: 40px; top: 126px; width: 180px;
    font-size: 14px; font-weight: 700; line-height: 23px;
    letter-spacing: 0.4px; text-transform: uppercase; color: var(--tan);
  }
  .intro-body {
    position: absolute; left: 40px; top: 312px; width: 168px;
    font-size: 10.4px; line-height: 15.4px; color: var(--text-grey); font-weight: 400;
  }
  .hero-photo {
    position: absolute; left: 233px; top: 43px; width: 317px; height: 435px;
    background: linear-gradient(180deg, #d9d9d9 0%, #a9a9a9 35%, #8e8e8e 60%, #6f6f6f 80%, #b9b9b9 100%);
  }
  .forest-photo {
    position: absolute; left: 39px; top: 504px; width: 168px; height: 114px;
    background: linear-gradient(135deg, #b5522a 0%, #d48a3a 35%, #6d8a3d 60%, #c7722f 100%);
  }
  .story-body {
    position: absolute; left: 233px; top: 503px; width: 268px;
    font-size: 10.4px; line-height: 15.4px; color: var(--text-grey);
  }
  .story-body strong { font-weight: 500; color: #6f6a68; }
  .page-number {
    position: absolute; left: 270px; top: 637px;
    font-size: 14px; color: #c9c6c3;
  }

  .collection-headline {
    position: absolute; left: 312px; top: 64px;
    font-size: 16px; font-weight: 400; line-height: 22px;
    letter-spacing: 0.6px; color: var(--page-white); text-transform: uppercase;
  }
  .product-render {
    position: absolute;
    background: rgba(255,255,255,0.12);
    border-radius: 2px;
  }
  .product-render--dining-table { left: 70px; top: 63px; width: 160px; height: 90px; }
  .product-render--short-bench { left: 70px; top: 243px; width: 130px; height: 70px; }
  .product-render--long-bench { left: 303px; top: 203px; width: 157px; height: 83px; }
  .product-render--shelf { left: 90px; top: 396px; width: 120px; height: 202px; }
  .product-render--coffee-table { left: 312px; top: 385px; width: 158px; height: 83px; }

  .signoff {
    position: absolute; left: 317px; top: 545px; color: var(--page-white);
  }
  .signoff__name { font-size: 30px; font-weight: 400; line-height: 34px; }
  .signoff__by { font-size: 8px; text-align: right; margin-top: 2px; }
</style>
</head>
<body>
  <div class="spread">
    <section class="page page--left">
      <div class="brand-name"><span class="brand-name__dot"></span>Brookvale</div>

      <h1 class="intro-headline">Kestrel Custom Plastics &amp; Acrylics, a Vancouver B.C. based company, is proud to launch the brand new Brookvale Furniture Collection.</h1>

      <p class="intro-body">From tables, chairs and benches, to corporate furniture, to shelves and coffee tables this unique suite of furniture is uniquely handsome and majestic. Each piece carries clean, rectangular lines and edges. Each remains faithful to the urban design ap&shy;peal yet showcases the natural warmth and softness of the wood hovering in the face of gravity.</p>

      <div class="hero-photo" role="img" aria-label="Black and white photo of a wooden beam bench suspended in clear acrylic, outdoors by a lake and pine tree"></div>
      <div class="forest-photo" role="img" aria-label="Aerial photo of an autumn forest in orange and green"></div>

      <p class="story-body">In keeping with Kestrel’s enduring philosophy, each piece of furniture is crafted from museum-quality materials - selected, fabricated and assembled by hand right here in B.C. Kestrel is the foremost manufacturer of high-end, custom, build-to-order acrylic and lucite furniture for both residential and commercial customers since 1978. The Brookvale <strong>Collection is the first to emerge from their new in-house designer</strong></p>

      <div class="page-number">4</div>
    </section>

    <section class="page page--right">
      <h2 class="collection-headline">Modern sustainable<br>furniture design.</h2>

      <div class="product-render product-render--dining-table" role="img" aria-label="Line drawing of dining table"></div>
      <div class="product-render product-render--short-bench" role="img" aria-label="Line drawing of short bench"></div>
      <div class="product-render product-render--long-bench" role="img" aria-label="Line drawing of long bench"></div>
      <div class="product-render product-render--shelf" role="img" aria-label="Line drawing of bookshelf"></div>
      <div class="product-render product-render--coffee-table" role="img" aria-label="Line drawing of coffee table"></div>

      <div class="signoff">
        <div class="signoff__name">Brookvale</div>
        <div class="signoff__by">by Kestrel</div>
      </div>
    </section>
  </div>
</body>
</html>
```